Create a Orvessa-looking dashboard for our Copper Lantern Speedometer that can look similar to my AI-generated dashboard attached, but with: 1) clear borders on all four sides, 2) is created in a way that we can modify the numbers weekly, say maybe you create the graphic that we can inset the excel spreadsheet numbers into, but ideally mixed with the Orvessa look black leather bubble design shown in the dashboard?; 3) uses the exact numbers shown in the attachment; 4) the speedometer on top should have four equal colors of red on left (-1), then yellow (0), then light green (1), then medium green (2); 5) the gauge on the top left should be the graphic that includes 0-100% bar that is currently 33%, and right below that a -20 to +20 bar with the arrow pointing to 11.9%, with color coding similar to the graphic; 6) replace the Orvessa logo in the middle with a similar shaped shield with blue background with the "T" logo with the eagle inside it, like attached

```html
<!DOCTYPE html>
<html lang="en">
<head>
<meta charset="utf-8">
<title>Copper Lantern Speedometer</title>
<link href="https://fonts.googleapis.com/css2?family=Orbitron:wght@500;700&family=Playfair+Display:wght@700;800&family=Roboto:wght@400;500;700&display=swap" rel="stylesheet">
<style>
  :root {
    --frame-black: #000;
    --frame-line: #d9d9d9;
    --leather: #b5161c;
    --leather-dark: #6a0a0e;
    --stitch: #f08a8a;
    --chrome: #d8d8d8;
    --chrome-dark: #6b6b6b;
    --panel: #151515;
    --panel-inner: #1f1f1f;
    --gold: #f2c230;
    --gauge-red: #d9231d;
    --gauge-yellow: #d8c41c;
    --gauge-light-green: #6fce3a;
    --gauge-green: #2f9e2c;
    --needle: #f4d43a;
    --header-blue: #0f2f8c;
    --bull: #3fcb58;
    --bullish: #93e0a3;
    --brakes: #f8f400;
    --reverse: #f01212;
    --reverse-text: #7a0000;
    --neutral-cell: #c6c6c6;
    --cell-text: #1a1a1a;
    --white: #ffffff;
  }
  * { box-sizing: border-box; margin: 0; padding: 0; }
  html, body { width: 1200px; height: 800px; overflow: hidden; background: var(--frame-black); }
  .dashboard {
    position: relative;
    width: 1200px;
    height: 800px;
    background: var(--frame-black);
    overflow: hidden;
  }
  .dashboard-art { position: absolute; inset: 0; }
  .dashboard-title {
    position: absolute;
    left: 0; right: 0;
    top: 404px;
    text-align: center;
    font-family: "Playfair Display", serif;
    font-weight: 800;
    font-size: 33px;
    letter-spacing: 0.2px;
    color: var(--gold);
    text-shadow: 0 2px 3px rgba(0,0,0,0.7);
  }
  .gear-table {
    position: absolute;
    left: 164px;
    top: 467px;
    width: 864px;
    display: grid;
    grid-template-columns: repeat(3, 281px);
    grid-template-rows: 41px repeat(4, 38px);
    column-gap: 10.5px;
    row-gap: 4px;
  }
  .gear-table .head {
    background: linear-gradient(#1a3fa6, var(--header-blue));
    color: var(--white);
    font-family: "Playfair Display", serif;
    font-weight: 700;
    font-size: 15px;
    display: flex; align-items: center; justify-content: center;
    margin-bottom: 2px;
  }
  .gear-table .cell {
    font-family: "Roboto", sans-serif;
    font-size: 16px;
    color: var(--cell-text);
    display: flex; align-items: center; justify-content: center;
    box-shadow: inset 0 0 0 1px rgba(0,0,0,0.15);
  }
  .gear-table .gear { justify-content: flex-start; padding-left: 47px; }
  .gear-turbo { background: var(--bull); }
  .gear-accel { background: var(--bullish); }
  .gear-brakes { background: var(--brakes); }
  .gear-reverse { background: var(--reverse); color: var(--reverse-text) !important; padding-left: 40px !important; }
  .is-active { background: var(--bull); }
  .is-idle { background: var(--neutral-cell); }
  .gauge-text { font-family: "Orbitron", sans-serif; fill: var(--white); }
</style>
</head>
<body>
<main class="dashboard">
  <svg class="dashboard-art" width="1200" height="800" viewBox="0 0 1200 800">
    <defs>
      <radialGradient id="leather-fill" cx="50%" cy="45%" r="70%">
        <stop offset="0" stop-color="#c81c22"/>
        <stop offset="0.7" stop-color="#a11318"/>
        <stop offset="1" stop-color="var(--leather-dark)"/>
      </radialGradient>
      <linearGradient id="chrome-fill" x1="0" y1="0" x2="0" y2="1">
        <stop offset="0" stop-color="#f4f4f4"/>
        <stop offset="0.5" stop-color="#9a9a9a"/>
        <stop offset="1" stop-color="#e2e2e2"/>
      </linearGradient>
      <radialGradient id="gauge-body" cx="50%" cy="40%" r="65%">
        <stop offset="0" stop-color="#2a2a2a"/>
        <stop offset="1" stop-color="#050505"/>
      </radialGradient>
      <radialGradient id="knob" cx="40%" cy="35%" r="70%">
        <stop offset="0" stop-color="#4a4a4a"/>
        <stop offset="1" stop-color="#070707"/>
      </radialGradient>
      <clipPath id="center-face-clip">
        <path d="M378 326 A222 222 0 0 1 822 326 Z"/>
      </clipPath>
    </defs>

    <!-- frame -->
    <rect x="22" y="13" width="1156" height="771" fill="url(#leather-fill)" stroke="var(--frame-line)" stroke-width="1" role="img" aria-label="Red stitched leather upholstery"/>

    <!-- stitching lines -->
    <g fill="none" stroke="var(--stitch)" stroke-width="1.3" stroke-dasharray="5 4" opacity="0.8">
      <path d="M22 132 L290 132 C350 132 380 66 460 62 L740 62 C820 66 850 132 910 132 L1178 132"/>
      <path d="M22 143 L292 143 C354 143 384 76 462 73 L738 73 C816 76 846 143 908 143 L1178 143"/>
      <path d="M22 226 C60 230 80 245 96 262"/>
      <path d="M1178 226 C1140 230 1120 245 1108 262"/>
      <path d="M90 395 Q300 372 600 364 Q900 372 1110 395"/>
      <path d="M92 718 L1108 718"/>
      <path d="M22 560 C50 560 70 570 90 585"/>
      <path d="M1178 560 C1150 560 1130 570 1110 585"/>
    </g>

    <!-- chrome trim band -->
    <path d="M22 180 L300 180 C360 180 380 98 460 94 L740 94 C820 98 840 180 900 180 L1178 180" fill="none" stroke="#3a0407" stroke-width="12" opacity="0.6"/>
    <path d="M22 177 L300 177 C360 177 380 95 460 91 L740 91 C820 95 840 177 900 177 L1178 177" fill="none" stroke="url(#chrome-fill)" stroke-width="6"/>

    <!-- carbon backing -->
    <rect x="300" y="192" width="600" height="160" rx="20" fill="#1d1d1d" stroke="#3a3a3a"/>

    <!-- left gauge: progress -->
    <g class="gauge-progress">
      <path d="M97 317 A120 120 0 0 1 337 317 L337 345 Q337 390 292 390 L142 390 Q97 390 97 345 Z" fill="url(#gauge-body)" stroke="url(#chrome-fill)" stroke-width="5"/>
      <g fill="none" stroke-width="8">
        <path d="M120 317 A95 95 0 0 1 138.1 261.1" stroke="#2fb53a"/>
        <path d="M138.1 261.1 A95 95 0 0 1 185.6 226.7" stroke="#8bcf2c"/>
        <path d="M185.6 226.7 A95 95 0 0 1 244.4 226.7" stroke="#f2d22a"/>
        <path d="M244.4 226.7 A95 95 0 0 1 291.9 261.1" stroke="#f08a1e"/>
        <path d="M291.9 261.1 A95 95 0 0 1 310 317" stroke="#e2261c"/>
      </g>
      <rect x="111" y="319" width="40" height="3" fill="#dcdcdc"/>
      <rect x="284" y="319" width="42" height="3" fill="#dcdcdc"/>
      <text class="gauge-text" x="215" y="277" text-anchor="middle" font-size="26" font-weight="700">33%</text>
      <text class="gauge-text" x="215" y="293" text-anchor="middle" font-size="11">(165/500)</text>
      <polygon points="216,320 214,314 132,299" fill="var(--needle)"/>
      <circle cx="215" cy="317" r="13" fill="url(#knob)" stroke="#555"/>
    </g>

    <!-- center gauge: gear -->
    <g class="gauge-gear">
      <path d="M366 330 A234 234 0 0 1 834 330" fill="none" stroke="url(#chrome-fill)" stroke-width="12"/>
      <path d="M378 326 L600 326 L443 169 A222 222 0 0 0 378 326 Z" fill="var(--gauge-red)"/>
      <path d="M443 169 L600 326 L600 104 A222 222 0 0 0 443 169 Z" fill="var(--gauge-yellow)"/>
      <path d="M600 104 L600 326 L757 169 A222 222 0 0 0 600 104 Z" fill="var(--gauge-light-green)"/>
      <path d="M757 169 L600 326 L822 326 A222 222 0 0 0 757 169 Z" fill="var(--gauge-green)"/>
      <g clip-path="url(#center-face-clip)" fill="none" stroke="#111">
        <circle cx="600" cy="326" r="214" stroke-width="10" stroke-dasharray="1.5 17.2"/>
        <circle cx="600" cy="326" r="207" stroke-width="22" stroke-dasharray="3.5 77.8" transform="rotate(-1 600 326)"/>
      </g>
      <rect x="370" y="326" width="460" height="18" fill="#1d1d1d"/>
      <text class="gauge-text" x="431" y="269" text-anchor="middle" font-size="22" font-weight="700">-01</text>
      <text class="gauge-text" x="532" y="180" text-anchor="middle" font-size="20" font-weight="700" fill="#111" style="fill:#111">0</text>
      <text class="gauge-text" x="663" y="180" text-anchor="middle" font-size="20" font-weight="700" style="fill:#111">01</text>
      <text class="gauge-text" x="767" y="269" text-anchor="middle" font-size="22" font-weight="700">02</text>

      <circle class="brand-badge" cx="600" cy="196" r="33" fill="#f4f4f4"/>
      <text x="600" y="193" text-anchor="middle" font-family="Roboto, sans-serif" font-weight="700" font-size="10" fill="#0f2f8c">
        <tspan x="600">Copper</tspan><tspan x="600" dy="12">Lantern</tspan>
      </text>

      <path d="M520 326 A80 80 0 0 1 680 326 Z" fill="#0b0b0b" stroke="url(#chrome-fill)" stroke-width="6"/>
      <polygon points="604.4,295.4 595.6,290.6 682,145" fill="var(--needle)"/>
      <circle cx="600" cy="293" r="22" fill="url(#knob)" stroke="#333"/>
    </g>

    <!-- right gauge: weekly change -->
    <g class="gauge-change">
      <ellipse cx="985" cy="300" rx="121" ry="96" fill="url(#gauge-body)" stroke="url(#chrome-fill)" stroke-width="5"/>
      <g fill="none" stroke-width="9">
        <path d="M903.5 247.3 A96 96 0 0 1 960.3 214.4" stroke="#3aa83a"/>
        <path d="M960.3 214.4 A96 96 0 0 1 1025 225.9" stroke="#78c25a"/>
        <path d="M1025 225.9 A96 96 0 0 1 1067.2 276.2" stroke="#b9d99a"/>
        <path d="M1067.2 276.2 A96 96 0 0 1 1067.2 341.8" stroke="#f2e08a"/>
        <path d="M1067.2 341.8 A96 96 0 0 1 1044.9 376.9" stroke="#f0c41e"/>
        <path d="M1044.9 376.9 A96 96 0 0 1 1025 392.1" stroke="#e2261c"/>
      </g>
      <g class="gauge-text" font-size="11" font-weight="500" style="fill:#dcdcdc">
        <text x="937" y="265" text-anchor="middle">20%</text>
        <text x="995" y="251" text-anchor="middle">10%</text>
        <text x="1041" y="276" text-anchor="middle">0%</text>
        <text x="1049" y="317" text-anchor="middle">-10%</text>
        <text x="1040" y="361" text-anchor="middle">-20%</text>
      </g>
      <text class="gauge-text" x="920" y="318" text-anchor="middle" font-size="23" font-weight="700">11.9%</text>
      <polygon points="979,311 975,307 1026,241" fill="var(--needle)"/>
      <circle cx="977" cy="309" r="14" fill="#1a1a1a"/>
    </g>

    <!-- lower panel -->
    <path d="M104 700 L104 470 Q104 446 130 441 Q300 400 600 382 Q900 400 1070 441 Q1097 446 1097 470 L1097 700 Q1097 711 1086 711 L115 711 Q104 711 104 700 Z" fill="var(--panel)" stroke="url(#chrome-fill)" stroke-width="4"/>
    <rect x="111" y="453" width="978" height="247" rx="24" fill="var(--panel-inner)" stroke="#5a5a5a" stroke-width="2"/>
  </svg>

  <h1 class="dashboard-title">COPPER LANTERN SPEEDOMETER</h1>

  <section class="gear-table">
    <div class="head">GEAR</div>
    <div class="head">CURRENT TREND</div>
    <div class="head">LAST TREND CHANGE</div>

    <div class="cell gear gear-turbo">2 TURBO BOOST</div>
    <div class="cell is-active">BULL</div>
    <div class="cell is-active">Friday, August 15, 2025</div>

    <div class="cell gear gear-accel">1 ACCELERATOR PEDAL</div>
    <div class="cell is-idle">BULLISH</div>
    <div class="cell is-idle"></div>

    <div class="cell gear gear-brakes">0 BRAKES</div>
    <div class="cell is-idle">BEARISH</div>
    <div class="cell is-idle"></div>

    <div class="cell gear gear-reverse">-1 REVERSE</div>
    <div class="cell is-idle">BEAR</div>
    <div class="cell is-idle"></div>
  </section>
</main>
</body>
</html>
```